New stationery for photographic studio - logo already designed
Business cards, letterhead, comp slips, DVD face
New stationery for photographic studio - logo already designed -
Creative Brief
Use specific fonts
Handel Gothic
Simple
Dale Hoskins
Photographer
42 Pellow Lane Fareham Hampshire PO16 8RT
dalehoskins@tarnbrookstudios.co.uk
www.tarnbrookstudios.co.uk
My logo features the company name next to it in the .ai file. Ideally I would like the logo to just be presented on it's own with the company name mentioned elsewhere (Tarnbrook Studios). I also have a separate website for my commercial work www.tarnbrookcommercial.co.uk - which I will likely want to print additional business cards for to get some separation from the other side of the business (portraits) but with exactly the same look and feel just a text change.
Some of my cards will features images and so I need a single sided card design. However, some of them will also have a plain back and I was looking to have variant with just a logo on the back

```html
<!DOCTYPE html>
<html lang="en">
<head>
<meta charset="utf-8">
<title>Tarnbrook Studios – Business Cards</title>
<link href="https://fonts.googleapis.com/css2?family=Michroma&family=Jura:wght@500;700&display=swap" rel="stylesheet">
<style>
  :root {
    --backdrop: #ececec;
    --card-light: #ffffff;
    --card-dark: #2a2a2a;
    --ink-dark: #1c1c1c;
    --ink-light: #f2f2f2;
    --ink-muted: #555555;
    --brand-blue: #7fa9d8;
    --brand-blue-pale: #d6e6f6;
    --brand-blue-deep: #4f7fb8;
  }
  html, body {
    margin: 0;
    width: 1200px;
    height: 871px;
    overflow: hidden;
    background: var(--backdrop);
  }
  .stationery {
    position: relative;
    width: 1200px;
    height: 871px;
  }
  .card {
    position: absolute;
    overflow: hidden;
    font-family: "Jura", sans-serif;
    color: var(--ink-dark);
    background: var(--card-light);
  }
  .card--small { width: 292px; height: 176px; font-size: 11.1px; }
  .card--large { width: 420px; height: 253px; font-size: 16px; }
  .card--dark { background: var(--card-dark); color: var(--ink-light); }

  .card--portrait-small { left: 336px; top: 244px; }
  .card--commercial-small { left: 643px; top: 244px; }
  .card--portrait-large { left: 174px; top: 470px; }
  .card--commercial-large { left: 628px; top: 470px; }

  .brand {
    position: absolute;
    left: 7%;
    top: 19%;
    width: 23%;
    text-align: center;
  }
  .brand__mark {
    display: block;
    width: 76%;
    aspect-ratio: 1;
    margin: 0 auto 0.5em;
    background: linear-gradient(160deg, var(--brand-blue-pale), var(--brand-blue) 70%, var(--brand-blue-deep));
  }
  .brand__name {
    font-family: "Michroma", sans-serif;
    font-size: 0.5em;
    line-height: 1.35;
    letter-spacing: 0.04em;
    text-transform: uppercase;
    color: var(--brand-blue-deep);
  }
  .card--dark .brand__name { color: var(--brand-blue); }

  .holder {
    position: absolute;
    right: 7%;
    top: 17%;
    text-align: right;
  }
  .holder__name {
    margin: 0;
    font-family: "Michroma", sans-serif;
    font-size: 1.35em;
    font-weight: 400;
    letter-spacing: 0.03em;
    text-transform: uppercase;
  }
  .holder__role {
    margin: 0.15em 0 0;
    font-size: 0.95em;
    font-weight: 700;
    color: var(--ink-muted);
  }
  .card--dark .holder__role { color: #cfcfcf; }

  .contact {
    position: absolute;
    right: 7%;
    top: 54%;
    margin: 0;
    padding: 0;
    list-style: none;
    text-align: right;
    font-size: 0.78em;
    font-weight: 700;
    line-height: 1.3;
  }
  .contact__email { margin-top: 0.7em; }
  .contact__web {
    position: absolute;
    right: 7%;
    bottom: 10%;
    font-size: 0.92em;
    font-weight: 700;
    letter-spacing: 0.02em;
  }

  .sweep {
    position: absolute;
    right: 0;
    bottom: 0;
    width: 62%;
    height: 30%;
    background: linear-gradient(170deg, transparent 35%, rgba(127,169,216,0.22) 60%, rgba(127,169,216,0.45));
  }
  .card--dark .sweep {
    background: linear-gradient(170deg, transparent 35%, rgba(127,169,216,0.2) 60%, rgba(127,169,216,0.4));
  }
</style>
</head>
<body>
<main class="stationery">

  <article class="card card--small card--portrait-small">
    <div class="sweep" role="img" aria-label="Soft blue wave decoration"></div>
    <div class="brand"><span class="brand__mark"></span><span class="brand__name">Tarnbrook<br>Studios</span></div>
    <div class="holder"><h2 class="holder__name">Dale Hoskins</h2><p class="holder__role">Photographer</p></div>
    <ul class="contact">
      <li>01329 584217</li>
      <li>07700 900462</li>
      <li class="contact__email">dalehoskins@tarnbrookstudios.co.uk</li>
    </ul>
    <div class="contact__web">www.tarnbrookstudios.co.uk</div>
  </article>

  <article class="card card--small card--dark card--commercial-small">
    <div class="sweep" role="img" aria-label="Soft blue wave decoration"></div>
    <div class="brand"><span class="brand__mark"></span><span class="brand__name">Tarnbrook<br>Studios</span></div>
    <div class="holder"><h2 class="holder__name">Dale Hoskins</h2><p class="holder__role">Commercial Photographer</p></div>
    <ul class="contact">
      <li>01329 584217</li>
      <li>07700 900462</li>
      <li class="contact__email">dalehoskins@tarnbrookstudios.co.uk</li>
    </ul>
    <div class="contact__web">www.tarnbrookcommercial.co.uk</div>
  </article>

  <article class="card card--large card--portrait-large">
    <div class="sweep" role="img" aria-label="Soft blue wave decoration"></div>
    <div class="brand"><span class="brand__mark"></span><span class="brand__name">Tarnbrook<br>Studios</span></div>
    <div class="holder"><h2 class="holder__name">Dale Hoskins</h2><p class="holder__role">Photographer</p></div>
    <ul class="contact">
      <li>01329 584217</li>
      <li>07700 900462</li>
      <li class="contact__email">dalehoskins@tarnbrookstudios.co.uk</li>
    </ul>
    <div class="contact__web">www.tarnbrookstudios.co.uk</div>
  </article>

  <article class="card card--large card--dark card--commercial-large">
    <div class="sweep" role="img" aria-label="Soft blue wave decoration"></div>
    <div class="brand"><span class="brand__mark"></span><span class="brand__name">Tarnbrook<br>Studios</span></div>
    <div class="holder"><h2 class="holder__name">Dale Hoskins</h2><p class="holder__role">Commercial Photographer</p></div>
    <ul class="contact">
      <li>01329 584217</li>
      <li>07700 900462</li>
      <li class="contact__email">dalehoskins@tarnbrookstudios.co.uk</li>
    </ul>
    <div class="contact__web">www.tarnbrookcommercial.co.uk</div>
  </article>

</main>
</body>
</html>
```